Business card for a business coach / management consultant

My logo has been done and now I need a business card. Deliverable needs to be a PDF to give to the printer. I want it single sided as I want the back side blank.
I prefer a white card with modern simple professional design.
Details are:
Tobias Wrenfield
B.Sc. (hons) FRTB CP MEGOL
14 Calloway Rd
Marlow Vale WA 6120
Australia
mobile 041 23 584 17
email tobias@corporatepathlane.com.au
skype tobiaswrenfield8
Small to medium size business owners
Business

```html
<!DOCTYPE html>
<html lang="en">
<head>
<meta charset="utf-8">
<title>Corporate Pathlane – Business Card</title>
<link rel="stylesheet" href="https://fonts.googleapis.com/css2?family=Open+Sans:wght@400;700;800&display=swap">
<style>
  :root {
    --page-bg: #e9e7e3;
    --card-bg: #ffffff;
    --brand-blue: #0d3f7a;
    --text-grey: #7a7c80;
    --icon-grey: #55585d;
  }
  html, body {
    margin: 0;
    padding: 0;
    width: 1200px;
    height: 675px;
    overflow: hidden;
    background: var(--page-bg);
    font-family: "Open Sans", Verdana, sans-serif;
  }
  .card {
    position: absolute;
    left: 160px;
    top: 68px;
    width: 880px;
    height: 538px;
    background: var(--card-bg);
    box-shadow: 0 6px 24px rgba(0,0,0,0.18);
    overflow: hidden;
  }
  .brand-mark {
    position: absolute;
    left: -70px;
    top: 170px;
    width: 420px;
    height: 420px;
    border-radius: 50%;
    background: var(--brand-blue);
  }
  .wordmark {
    position: absolute;
    left: 420px;
    top: 40px;
    margin: 0;
    font-weight: 800;
    font-size: 56px;
    line-height: 56px;
    letter-spacing: -0.5px;
    color: var(--brand-blue);
  }
  .details {
    position: absolute;
    left: 440px;
    top: 230px;
    font-size: 17px;
    line-height: 23px;
    color: var(--text-grey);
  }
  .person-name {
    margin: 0;
    font-weight: 700;
    font-size: 22px;
    line-height: 26px;
    color: var(--brand-blue);
  }
  .credentials { margin: 0 0 24px; }
  .address { margin: 0 0 16px; font-style: normal; }
  .contact-list { list-style: none; margin: 0; padding: 0; }
  .contact-list li { display: flex; align-items: center; gap: 8px; }
  .contact-icon { width: 15px; height: 15px; fill: var(--icon-grey); flex: none; }
</style>
</head>
<body>
  <article class="card">
    <div class="brand-mark" role="img" aria-label="Corporate Pathlane brand circle"></div>

    <h1 class="wordmark">Corporate<br>Pathlane</h1>

    <section class="details">
      <h2 class="person-name">Tobias Wrenfield</h2>
      <p class="credentials">B.Sc. (hons) FRTB CP MEGOL</p>
      <address class="address">14 Calloway Rd<br>Marlow Vale WA 6120<br>Australia</address>
      <ul class="contact-list">
        <li>
          <svg class="contact-icon" viewBox="0 0 16 16" aria-hidden="true"><path d="M3.5 1.5l2.5 0 1.2 3.3-1.7 1.2a9 9 0 0 0 4.5 4.5l1.2-1.7 3.3 1.2 0 2.5a1.5 1.5 0 0 1-1.5 1.5A12.5 12.5 0 0 1 2 3a1.5 1.5 0 0 1 1.5-1.5z"/></svg>
          <span>041 23 584 17</span>
        </li>
        <li>
          <svg class="contact-icon" viewBox="0 0 16 16" aria-hidden="true"><path d="M1 3h14v10H1z M2 4.2v.5l6 4 6-4v-.5z" fill-rule="evenodd"/></svg>
          <span>tobias@corporatepathlane.com.au</span>
        </li>
        <li>
          <svg class="contact-icon" viewBox="0 0 16 16" aria-hidden="true"><circle cx="8" cy="8" r="7"/></svg>
          <span>tobiaswrenfield8</span>
        </li>
      </ul>
    </section>
  </article>
</body>
</html>
```